Bref créative
Fun, professional business cards/advertisment for dog boarding kennel
Bright Meadow Dog Boarding
I need double sided standard sized Business Card [3.5" x 2"]
Papyrus (name) and cambria (other type)
Bright & Fun-filled
Renata & Gideon - Certified Dog Lovers
481 Palomar Lane
Yellowknife, NT
brightmeadow@pawmail.example
http://www.brightmeadowdogboarding.example
Daily, weekly, monthly dog boarding.
Multi-dog discounts
Doggie day camp and overnight boarding
Individualized care, affordable rates
Formally Furlough Pet Camp & Boarding
Call to schedule services today!
On the back of the business cards we would like it quite simple- just the logo with our website and phone number
We would like the front to be able to be used as an advertisement....like made into a magnet, so on the front we would like our name, logo and small bullet points as noted in the other comments.
We would like a fun, happy, but simple appearance. Please keep the fonts the same as in the logo.
fonts to use
AI file of our logo as requested

```html
<!DOCTYPE html>
<html lang="en">
<head>
<meta charset="utf-8">
<title>Bright Meadow Dog Boarding – Business Cards</title>
<link rel="stylesheet" href="https://fonts.googleapis.com/css2?family=Caladea:ital,wght@0,400;0,700;1,400&family=Oswald:wght@600&display=swap">
<style>
  :root {
    --backdrop: #3b3b3d;
    --card: #ffffff;
    --brand-blue: #2f78b7;
    --brand-blue-soft: #d8e7f4;
    --brand-red: #d5402f;
    --ink: #3d3d3d;
    --muted: #6b6b6b;
  }
  * { box-sizing: border-box; margin: 0; padding: 0; }
  html, body { width: 1200px; height: 874px; overflow: hidden; }
  body {
    background: var(--backdrop);
    font-family: "Caladea", Georgia, serif;
    display: flex;
    align-items: center;
    justify-content: center;
    gap: 50px;
  }
  .card {
    position: relative;
    width: 525px;
    height: 300px;
    background: var(--card);
    border-radius: 16px;
    overflow: hidden;
    box-shadow: 0 10px 24px rgba(0,0,0,.35);
  }

  /* Advertisement side */
  .ad-card { display: flex; align-items: center; padding: 0 30px 0 28px; gap: 22px; }
  .ad-card .website {
    writing-mode: vertical-rl;
    transform: rotate(180deg);
    white-space: nowrap;
    font-family: "Oswald", "Arial Narrow", sans-serif;
    font-size: 10.5px;
    letter-spacing: 1.2px;
    color: var(--brand-blue);
    font-weight: 600;
    flex: none;
  }
  .ad-card .body { flex: 1; text-align: center; }
  .brand-mark {
    display: inline-flex;
    align-items: center;
    gap: 10px;
    font-size: 23px;
    color: var(--brand-blue);
    margin-bottom: 16px;
  }
  .brand-mark .dot {
    width: 20px; height: 20px; border-radius: 50%;
    background: var(--brand-blue-soft);
    border: 2px solid var(--brand-blue);
    flex: none;
  }
  .services { list-style: none; color: var(--brand-blue); font-style: italic; font-size: 14px; line-height: 1.55; }

  /* Contact side */
  .contact-card .band {
    position: absolute; right: 0; top: 0; width: 100%; height: 100%;
  }
  .contact-card .logo {
    position: absolute; right: 34px; top: 52px; width: 200px; text-align: left;
  }
  .contact-card .logo-name { font-size: 28px; line-height: 1.1; color: var(--brand-red); }
  .contact-card .tagline { font-size: 9px; color: var(--muted); margin-top: 6px; font-style: italic; }
  .contact-card .people { position: absolute; left: 34px; top: 62px; }
  .people h2 {
    font-family: "Oswald", "Arial Narrow", sans-serif;
    font-weight: 600; font-size: 23px; color: var(--brand-red); letter-spacing: .5px;
  }
  .people p { font-style: italic; color: var(--brand-red); font-size: 14px; }
  .contact { position: absolute; left: 34px; bottom: 34px; font-size: 12.5px; color: var(--ink); line-height: 1.5; }
  .contact li { list-style: none; display: flex; align-items: center; gap: 7px; }
  .contact .address { margin-bottom: 6px; }
  .contact svg { width: 12px; height: 12px; flex: none; }
</style>
</head>
<body>

  <section class="card ad-card" aria-label="Advertisement side">
    <div class="website">WWW.BRIGHTMEADOWDOGBOARDING.EXAMPLE</div>
    <div class="body">
      <div class="brand-mark"><span class="dot"></span>Bright Meadow Dog Boarding</div>
      <ul class="services">
        <li>~ Daily, weekly, monthly dog boarding ~</li>
        <li>~ Multi-dog discounts ~</li>
        <li>~ Doggie day camp and overnight boarding ~</li>
        <li>~ Individualized care, affordable rates ~</li>
        <li>~ Formally Furlough Pet Camp &amp; Boarding ~</li>
        <li>~ Call to schedule services today! ~</li>
      </ul>
    </div>
  </section>

  <section class="card contact-card" aria-label="Contact side">
    <svg class="band" viewBox="0 0 525 300" preserveAspectRatio="none" aria-hidden="true">
      <path d="M525 150 C470 240 380 275 300 300 L525 300 Z" fill="var(--brand-blue)"/>
    </svg>
    <div class="logo">
      <div class="logo-name">Bright Meadow Dog Boarding</div>
      <div class="tagline">Caring for pups with love and fun</div>
    </div>
    <div class="people">
      <h2>RENATA &amp; GIDEON</h2>
      <p>Certified Dog Lovers</p>
    </div>
    <ul class="contact">
      <li class="address">481 Palomar Lane<br>Yellowknife, NT</li>
      <li><svg viewBox="0 0 12 12"><path d="M3 1l2 2-1 1.5c.8 1.5 2 2.7 3.5 3.5L9 7l2 2-1.5 2C5 11 1 7 1 2.5z" fill="var(--brand-red)"/></svg>867-555-0142</li>
      <li><svg viewBox="0 0 12 12"><rect x="1" y="2.5" width="10" height="7" rx="1" fill="none" stroke="var(--brand-red)" stroke-width="1.2"/><path d="M1.5 3l4.5 3.5L10.5 3" fill="none" stroke="var(--brand-red)" stroke-width="1.2"/></svg>brightmeadow@pawmail.example</li>
      <li><svg viewBox="0 0 12 12"><circle cx="6" cy="6" r="5" fill="var(--brand-red)"/></svg>bright_mdow</li>
      <li><svg viewBox="0 0 12 12"><circle cx="6" cy="6" r="4.8" fill="none" stroke="var(--brand-red)" stroke-width="1.2"/><path d="M1.2 6h9.6M6 1.2c-2.4 3-2.4 6.6 0 9.6M6 1.2c2.4 3 2.4 6.6 0 9.6" fill="none" stroke="var(--brand-red)"/></svg>www.brightmeadowdogboarding.example</li>
    </ul>
  </section>

</body>
</html>
```